Vita Shield Prime is a new Chinese herbal medicine nutritional supplement.

I need a label design for my Dr Penwick Rx Chinese herbal supplement line .
I am launching a new super powerful immune booster
Vita Shield Prime.
The FRONT label 3 in. x 4 in. Black mylar bag will have 30 capsules
The Back label will be the size 3 inches x 3 inches will send information
Target Market(s)
Females 25 to 80 who buy nutritional supplements for themselves and their families.
Industry/Entity Type
Medicine
Font styles to use
Decorative
Colors
Designer to choose colors to be used in the design.
Requirements
Must have
- Dr Penwick Rx the name of the company. A wax seal with the an imprint of the name stamp letters on wax .. examples will be provided below.. an image of name stamp inside wax seal. Product name is Vita Shield Prime. Must use traditional Chinese colors. COLORS BELOW IN SAVED IMAGES.. GOLD, BLOOD RED, DARK PURPLE. description of product... Powerful Immune Booster.. a clear and easy to read label. ALL SO BACK LABEL 3 INCHES X 3 INCHES USING ONLY TWO COLORS.. BASIC PRODUCT LABEL OF INGREDIENTS, SUGGESTED USE, PRODUCT INFO, AND WARNINGS. IMAGES FILE 3 IS TO BE USED IN WAX SEAL.USE ONLY EXAMPLE COLORS BELOW IN IMAGES
Nice to have
- I like royal colors of ancient China, which happen to be strong psychological colors for marketing. A Gold wax with my name stamp in red or something like that. "Ancient Chinese secret for modern health".
Should not have

```html
<!DOCTYPE html>
<html lang="en">
<head>
<meta charset="utf-8">
<title>Vita Shield Prime – Front Label</title>
<link rel="stylesheet" href="https://fonts.googleapis.com/css2?family=Exo+2:ital,wght@0,800;1,800;1,900&display=swap">
<style>
  :root {
    --page: #ffffff;
    --label-red: #d93a0c;
    --seal-red: #c8290f;
    --gold: #fcee1c;
    --ink: #111111;
  }
  html, body {
    margin: 0;
    padding: 0;
    width: 1200px;
    height: 1200px;
    overflow: hidden;
    background: var(--page);
  }
  .canvas {
    position: relative;
    width: 1200px;
    height: 1200px;
  }
  .front-label {
    position: absolute;
    left: 195px;
    top: 60px;
    width: 810px;
    height: 1080px;
  }
  .label-ground { fill: var(--label-red); }
  .gold-panel { fill: var(--gold); }
  .seal-dot { fill: var(--seal-red); }
  .brand-name {
    font-family: "Exo 2", sans-serif;
    font-weight: 800;
    font-style: normal;
    fill: var(--seal-red);
  }
  .product-name {
    font-family: "Exo 2", sans-serif;
    font-weight: 900;
    font-style: italic;
    fill: var(--gold);
  }
  .tagline,
  .count {
    font-family: "Exo 2", sans-serif;
    font-weight: 800;
    font-style: italic;
    fill: var(--ink);
  }
</style>
</head>
<body>
<main class="canvas">
  <svg class="front-label" viewBox="0 0 400 533" xmlns="http://www.w3.org/2000/svg" aria-label="Vita Shield Prime front label">
    <rect class="label-ground" x="0" y="0" width="400" height="533"/>

    <path class="gold-panel top-arch" d="M15 267 V225 A185 185 0 0 1 385 225 V267 Z"/>
    <path class="gold-panel bottom-panel" d="M15 355 H385 V430 Q385 497 318 497 H82 Q15 497 15 430 Z"/>

    <g class="brand-mark">
      <circle class="seal-dot" cx="204" cy="112" r="62"/>
      <text class="brand-name" x="204" y="222" text-anchor="middle" font-size="30">Dr Penwick Rx's</text>
    </g>

    <g class="product-title">
      <text class="product-name" x="200" y="298" text-anchor="middle" font-size="31">VITA SHIELD</text>
      <text class="product-name" x="200" y="343" text-anchor="middle" font-size="46">PRIME</text>
    </g>

    <g class="product-tagline">
      <text class="tagline" x="93" y="410" font-size="26">Powerful</text>
      <text class="tagline" x="128" y="437" font-size="26">Immune</text>
      <text class="tagline" x="163" y="464" font-size="26">Booster</text>
    </g>

    <g class="capsule-count">
      <text class="count" x="355" y="490" text-anchor="middle" font-size="18">30</text>
      <text class="count" x="350" y="506" text-anchor="middle" font-size="10">capsules</text>
    </g>
  </svg>
</main>
</body>
</html>
```